Ready Ranks: Marching Beside The Quiet Flame

I'm thinking a main imagery having to do with dog tags

The series is April 8th-May 20th (this would go on the facebook cover page and instagram posts)

Main graphic background slide (for main points to be written on) 1920×1080
Main graphic Slide Title 1920×1080
Facebook cover page 851×315
Instagram Posts 1200×1200

Attached are some examples of what can be used and incorporated. I'll also include our logo if you want to incorporate somehow but it's not mandatory by any stretch.

Target Market(s)

people who don't go to church or may have not been in a while

Industry/Entity Type

Church

Font styles to use
Decorative

Colors

Designer to choose colors to be used in the design.

Requirements
Must have
• some military imagery but not too much where it's a turn off.
Nice to have
• Some element of The Holy Spirit mixed in.
Should not have
• Not look too church

```html
<!DOCTYPE html>
<html lang="en">
<head>
<meta charset="utf-8">
<title>Ready Ranks: Marching Beside The Quiet Flame</title>
<link rel="stylesheet" href="https://fonts.googleapis.com/css2?family=Rubik+Dirt&family=Stardos+Stencil:wght@700&display=swap">
<style>
  :root {
    --plate-black: #0d0d0e;
    --plate-dark: #1c1c1e;
    --plate-mid: #343437;
    --plate-light: #4a4a4e;
    --ink-white: #f2f2f2;
    --flame-orange: #f4a21c;
    --flame-gold: #f8b83f;
    --tag-steel-light: #e4e5e6;
    --tag-steel-mid: #b4b6b8;
    --tag-steel-dark: #808285;
  }
  * { margin: 0; padding: 0; box-sizing: border-box; }
  html, body { width: 1200px; height: 449px; overflow: hidden; background: var(--plate-black); }
  .cover {
    position: relative;
    width: 1200px;
    height: 449px;
    overflow: hidden;
  }
  .plate-background {
    position: absolute;
    inset: 0;
    background:
      radial-gradient(ellipse 70% 80% at 45% 45%, var(--plate-light) 0%, var(--plate-mid) 35%, var(--plate-dark) 70%, var(--plate-black) 100%);
  }
  .header-rule {
    position: absolute;
    top: 16px;
    left: 360px;
    width: 501px;
    height: 26px;
  }
  .cross-mark {
    position: absolute;
    top: 98px;
    width: 50px;
    height: 76px;
    border-radius: 3px;
    background: linear-gradient(180deg, var(--flame-gold), var(--flame-orange));
  }
  .cross-mark.left { left: 124px; }
  .cross-mark.right { left: 1048px; }
  .series-title {
    position: absolute;
    top: 44px;
    left: 0;
    width: 1200px;
    text-align: center;
    white-space: nowrap;
    font-family: "Rubik Dirt", sans-serif;
    font-weight: 400;
    font-size: 112px;
    line-height: 1.1;
    letter-spacing: 2px;
    color: var(--ink-white);
  }
  .series-subtitle {
    position: absolute;
    top: 172px;
    left: 0;
    width: 1200px;
    text-align: center;
    white-space: nowrap;
    font-family: "Stardos Stencil", serif;
    font-weight: 700;
    font-size: 48px;
    line-height: 1.2;
    letter-spacing: 1px;
    color: var(--flame-orange);
  }
  .series-dates {
    position: absolute;
    top: 246px;
    left: 560px;
    width: 480px;
    text-align: center;
    white-space: nowrap;
    font-family: "Stardos Stencil", serif;
    font-weight: 700;
    font-size: 42px;
    line-height: 1.2;
    letter-spacing: 1px;
    color: var(--ink-white);
  }
  .series-dates sup { font-size: 0.5em; vertical-align: 0.9em; }
  .dog-tag {
    position: absolute;
    left: 190px;
    top: 326px;
    width: 216px;
    height: 112px;
    border-radius: 30px;
    transform: rotate(-16deg);
    background: linear-gradient(160deg, var(--tag-steel-light) 0%, var(--tag-steel-mid) 55%, var(--tag-steel-dark) 100%);
    box-shadow: 4px 6px 10px rgba(0, 0, 0, 0.55);
  }
</style>
</head>
<body>
  <main class="cover">
    <div class="plate-background" role="img" aria-label="Dark steel diamond-plate texture"></div>

    <svg class="header-rule" viewBox="0 0 501 26" aria-hidden="true">
      <rect x="0" y="14" width="222" height="3" fill="#f2f2f2"/>
      <rect x="279" y="14" width="222" height="3" fill="#f2f2f2"/>
      <polygon fill="#f2f2f2" points="233,7 235.4,11.8 240.6,12.5 236.8,16 237.8,21 233,18.6 228.2,21 229.2,16 225.4,12.5 230.6,11.8"/>
      <polygon fill="#f2f2f2" points="250.5,2 253.6,8.4 260.5,9.3 255.5,14 256.8,21 250.5,17.7 244.2,21 245.5,14 240.5,9.3 247.4,8.4"/>
      <polygon fill="#f2f2f2" points="268,7 270.4,11.8 275.6,12.5 271.8,16 272.8,21 268,18.6 263.2,21 264.2,16 260.4,12.5 265.6,11.8"/>
    </svg>

    <div class="cross-mark left" role="img" aria-label="Orange ornamental cross"></div>
    <div class="cross-mark right" role="img" aria-label="Orange ornamental cross"></div>

    <h1 class="series-title">READY RANKS</h1>
    <p class="series-subtitle">MARCHING BESIDE THE QUIET FLAME</p>
    <p class="series-dates">APRIL 8<sup>TH</sup>-MAY 20<sup>TH</sup></p>

    <div class="dog-tag" role="img" aria-label="Embossed steel military dog tag hanging from a ball chain"></div>
  </main>
</body>
</html>
```